Corporate Identity Pack - LetterHead, Business Card, Envelope

We are looking for a clean, professional, and visually connected corporate identity set for our company "VELTA HOME" (Cleaning, Gardening, and Pest Control services).

The pack must include:

Business Card (front and back)
Envelope with recipient window on the right side (22x11)
A4 Letterhead

We provide:
Our final logo (PNG)
Three design references (Inspiration1, Inspiration2, Inspiration3) to spark ideas — but you are absolutely free to propose your own creative solutions based on these concepts.

What we want:
A clean, modern, and trustworthy style
A subtle but creative watermark or graphic detail on the letterhead (not too invasive)

The same visual "family feeling" across business card, envelope, and letterhead: designs must be different but clearly connected

Strong readability for all text and contact details

Use our brand colors (Navy Blue, Green, Orange/Red) in a smart, non-overloaded way

No strict limitations: we are open to creative proposals as long as they are coherent, elegant, and suitable for professional use

Technical specifications:
100% full A4 page layout (no accidental borders)

Deliver ready-to-print PDFs and vector files (AI, EPS)

Respect 5 mm safety margins

Standard sizes for A4, business card, envelope C6 with window at the right

Tone:
Modern – Clean – Elegant – Creative – Trustworthy

Target Market(s)

Professional businesses, property managers, condominium administrators, companies, clinics, and offices requiring cleaning, gardening, and pest control services. The design must convey trust, reliability, professionalism, and attention to detail.

Industry/Entity Type

Cleaning Services, Gardening Services, Pest Control Services

Colors
0054AA
0677BA
7BADD7
CADEEF
E8F1F8
59FF00
82FF00
B8FF75
E3FFCB
F4FFEA
EB3D1F
EC4F4E
F09395
F8D3D4
FCEDEE

Requirements
Must have
• Cohesive design across business card, letterhead, and envelope Clean, modern, professional look Use of brand colors: Navy Blue (main), Green, Orange/Red accents Letterhead must include a subtle watermark without interfering with text Envelope must be with a transparent window for recipient address visibility High readability of all text and contact details Proper alignment, no unnecessary margins (full A4 layout)
Nice to have
• Creative but discreet use of the checkmark from the logo as part of the background or watermark Slight variation or accent of color tones while respecting brand identity A clean visual accent that gives a sense of movement or dynamic professionalism (without being distracting) Icons for email, phone, and website on the business card (if stylistically appropriate)
Should not have
• Overuse of colors or rainbow effects Heavy backgrounds or complex textures that interfere with readability Fonts that are too playful, comic-style, or non-professional Overcrowded layouts — the design must feel clean and spacious Watermarks that are too strong or central (they must be subtle and marginal)

```html
<!DOCTYPE html>
<html lang="en">
<head>
<meta charset="utf-8">
<title>Velta Home – Letterhead</title>
<link rel="stylesheet" href="https://fonts.googleapis.com/css2?family=Montserrat:wght@500;600&family=Arimo:wght@400&display=swap">
<style>
  :root {
    --navy: #1a0ff0;
    --ink: #1a1a1a;
    --band-blue: #8a88fb;
    --band-orange: #ffae8a;
    --band-green: #b7ff85;
    --paper: #fefefe;
    --mark-blue: #edebfd;
    --mark-green: #f1fdea;
  }
  * { margin: 0; padding: 0; box-sizing: border-box; }
  html, body { width: 849px; height: 1200px; overflow: hidden; background: var(--paper); }
  .letterhead { position: relative; width: 849px; height: 1200px; background: var(--paper); overflow: hidden; }

  .corner-accent {
    position: absolute; top: 0; right: 0; width: 440px; height: 370px;
    background: linear-gradient(215deg,
      rgba(250,190,165,.45) 0%,
      rgba(205,245,195,.42) 40%,
      rgba(225,248,255,.40) 65%,
      rgba(240,255,235,.25) 85%,
      rgba(255,255,255,0) 100%);
    clip-path: polygon(0 24%, 16% 0, 100% 0, 100% 100%, 62% 66%, 25% 48%);
  }

  .brand { position: absolute; left: 57px; top: 52px; display: flex; align-items: flex-start; gap: 18px; }
  .brand-square { width: 46px; height: 46px; background: var(--navy); margin-top: 4px; }
  .brand-name {
    font-family: "Montserrat", sans-serif; font-weight: 600; font-size: 37px;
    line-height: 38px; color: var(--navy); letter-spacing: .3px;
  }
  .brand-tagline {
    font-family: "Montserrat", sans-serif; font-weight: 500; font-size: 10.5px;
    letter-spacing: 1.45px; color: var(--navy); margin-top: 4px; white-space: nowrap;
  }

  .contacts { position: absolute; left: 601px; top: 41px; list-style: none;
    font-family: "Arimo", Arial, sans-serif; font-size: 13px; line-height: 14.5px; color: var(--ink); }
  .contacts li { display: flex; align-items: center; height: 14.5px; gap: 5px; white-space: nowrap; }
  .contact-icon { width: 19px; display: flex; justify-content: center; flex: none; }
  .contact-icon svg { display: block; }

  .watermark { position: absolute; left: 350px; top: 557px; width: 172px; height: 173px;
    background: linear-gradient(160deg, var(--mark-blue) 0%, #f4f6fe 55%, var(--mark-green) 100%);
    opacity: .85; }

  .footer-bands { position: absolute; left: 0; bottom: 0; height: 14px; display: flex; }
  .band { height: 100%; }
  .band--blue { width: 108px; background: var(--band-blue); }
  .band--orange { width: 129px; background: var(--band-orange); }
  .band--green { width: 101px; background: var(--band-green); }
</style>
</head>
<body>
<main class="letterhead">
  <div class="corner-accent" role="img" aria-label="Soft overlapping translucent tiles in blue, green and orange tones"></div>

  <header class="brand">
    <div class="brand-square"></div>
    <div>
      <div class="brand-name">VELTA HOME</div>
      <div class="brand-tagline">CLEANING·GARDENING·PESTCONTROL</div>
    </div>
  </header>

  <ul class="contacts">
    <li><span class="contact-icon"><svg width="11" height="11" viewBox="0 0 11 11"><circle cx="5.5" cy="5.5" r="5.5" fill="#1a0ff0"/><path d="M4 3 L5 4.5 L4.3 5.2 Q5 6.5 6 6.8 L6.7 6 L8 7 L7.3 8 Q4 7.8 3 4 Z" fill="#fff"/></svg></span>+39 320 555 0147</li>
    <li><span class="contact-icon"><svg width="11" height="11" viewBox="0 0 11 11"><circle cx="5.5" cy="5.5" r="5.5" fill="#1a0ff0"/><rect x="2.8" y="3.6" width="5.4" height="3.8" fill="none" stroke="#fff" stroke-width=".7"/><path d="M2.8 3.6 L5.5 5.8 L8.2 3.6" fill="none" stroke="#fff" stroke-width=".7"/></svg></span>office@veltahome.example</li>
    <li><span class="contact-icon"><svg width="11" height="11" viewBox="0 0 11 11"><circle cx="5.5" cy="5.5" r="5.5" fill="#1a0ff0"/><circle cx="5.5" cy="5.5" r="3" fill="none" stroke="#fff" stroke-width=".6"/><path d="M2.5 5.5 H8.5 M5.5 2.5 V8.5" stroke="#fff" stroke-width=".6"/></svg></span>www.veltahome.example</li>
    <li><span class="contact-icon"><svg width="19" height="9" viewBox="0 0 19 9"><rect x=".5" y=".5" width="18" height="8" rx="4" fill="none" stroke="#1a0ff0"/><rect x="3" y="3" width="13" height="3" fill="#1a0ff0"/></svg></span>info.veltahome@pec.example</li>
    <li><span class="contact-icon"><svg width="19" height="9" viewBox="0 0 19 9"><rect x=".5" y=".5" width="18" height="8" rx="4" fill="none" stroke="#1a0ff0"/><rect x="3" y="3" width="13" height="3" fill="#1a0ff0"/></svg></span>K7TQZB4</li>
  </ul>

  <div class="watermark"></div>

  <footer class="footer-bands">
    <div class="band band--blue"></div>
    <div class="band band--orange"></div>
    <div class="band band--green"></div>
  </footer>
</main>
</body>
</html>
```